Brivond Technologies business card design

We need a business card designed with our new logo. it would be great if the card could communicate it is a technology based company.

Target Market(s)

system integrators

Industry/Entity Type

technology, IOT

Contact Information for Business Card

Name, designation, Address, telephone number, email address

Requirements
Must have
• logo and company name
Nice to have
• something to do with technology

```html
<!DOCTYPE html>
<html lang="en">
<head>
<meta charset="utf-8">
<title>Brivond Technologies business card</title>
<link rel="stylesheet" href="https://fonts.googleapis.com/css2?family=Roboto:wght@400;700&display=swap">
<style>
  :root {
    --stage: #e6e4e1;
    --card-light: #ffffff;
    --card-dark: #3a3a3d;
    --ink: #3a3a3d;
    --ink-soft: #55555a;
    --ink-faint: #ececec;
    --accent: #ef8f1c;
    --on-dark: #ffffff;
  }
  * { box-sizing: border-box; margin: 0; padding: 0; }
  html, body { width: 1200px; height: 716px; overflow: hidden; }
  body {
    background: var(--stage);
    font-family: "Roboto", Arial, sans-serif;
    position: relative;
  }
  .card {
    position: absolute;
    top: 200px;
    width: 540px;
    height: 316px;
    box-shadow: 0 6px 18px rgba(0,0,0,0.18);
    overflow: hidden;
  }
  .card-front { left: 40px; background: var(--card-light); color: var(--ink); }
  .card-back  { left: 620px; background: var(--card-dark); color: var(--on-dark); }

  .bands { position: absolute; inset: 0; width: 540px; height: 316px; }
  .band-dark { fill: var(--card-dark); }
  .band-accent { fill: var(--accent); }
  .band-light { fill: var(--on-dark); }

  .brand {
    display: flex;
    align-items: center;
    gap: 10px;
    font-weight: 700;
    letter-spacing: 0.04em;
    text-transform: uppercase;
    white-space: nowrap;
  }
  .brand-mark { width: 14px; height: 14px; background: var(--accent); flex: none; }
  .card-front .brand { position: absolute; left: 40px; top: 36px; font-size: 18px; color: var(--ink); }

  .holder { position: absolute; left: 40px; top: 86px; }
  .holder-name { font-size: 19px; font-weight: 700; color: var(--accent); }
  .holder-role { font-size: 12px; color: var(--ink-soft); margin-top: 2px; }

  .address { position: absolute; left: 40px; top: 138px; font-size: 12px; line-height: 1.5; color: var(--ink-soft); }

  .contacts { position: absolute; left: 40px; top: 184px; list-style: none; font-size: 12px; color: var(--ink-soft); }
  .contacts li { display: flex; align-items: center; gap: 8px; line-height: 19px; }
  .contacts svg { width: 11px; height: 11px; flex: none; }

  .site-faint {
    position: absolute; left: 150px; top: 278px;
    font-size: 11px; letter-spacing: 0.2em; color: var(--ink-faint);
  }

  .card-back .brand {
    position: absolute; right: 40px; bottom: 56px;
    font-size: 30px; color: var(--on-dark);
  }
  .card-back .brand-mark { width: 20px; height: 20px; }
</style>
</head>
<body>
  <section class="card card-front" aria-label="Card front">
    <svg class="bands" viewBox="0 0 540 316" aria-hidden="true">
      <polygon class="band-dark" points="320,316 420,130 540,130 540,316"/>
      <polygon class="band-accent" points="432,112 492,0 530,0 470,112"/>
    </svg>
    <div class="brand"><span class="brand-mark"></span>Brivond Technologies</div>
    <div class="holder">
      <p class="holder-name">Marcus Ellery</p>
      <p class="holder-role">Managing Director</p>
    </div>
    <p class="address">4210 Larkspur Road<br>Fairbanks, Alaska 34512</p>
    <ul class="contacts">
      <li><svg viewBox="0 0 12 12" aria-hidden="true"><path fill="var(--accent)" d="M2.5 1h2l1 3-1.5 1a6 6 0 0 0 3 3l1-1.5 3 1v2a1 1 0 0 1-1 1A9.5 9.5 0 0 1 1.5 2a1 1 0 0 1 1-1z"/></svg>555-218-4470</li>
      <li><svg viewBox="0 0 12 12" aria-hidden="true"><rect x="3" y="0.5" width="6" height="11" rx="1" fill="none" stroke="var(--accent)" stroke-width="1.2"/><circle cx="6" cy="9.5" r="0.7" fill="var(--accent)"/></svg>555-302-9186</li>
      <li><svg viewBox="0 0 12 12" aria-hidden="true"><rect x="0.5" y="2.5" width="11" height="7" fill="var(--accent)"/><path d="M0.5 2.5 6 6.5l5.5-4" fill="none" stroke="#fff" stroke-width="1"/></svg>info@brivond.com</li>
      <li><svg viewBox="0 0 12 12" aria-hidden="true"><circle cx="6" cy="6" r="5.2" fill="none" stroke="var(--accent)" stroke-width="1.2"/><path d="M0.8 6h10.4M6 0.8c-2.5 3-2.5 7.4 0 10.4M6 0.8c2.5 3 2.5 7.4 0 10.4" fill="none" stroke="var(--accent)" stroke-width="0.9"/></svg>www.brivond.com</li>
    </ul>
    <p class="site-faint">www.brivond.com</p>
  </section>

  <section class="card card-back" aria-label="Card back">
    <svg class="bands" viewBox="0 0 540 316" aria-hidden="true">
      <polygon class="band-light" points="0,262 110,150 160,150 0,312"/>
      <polygon class="band-accent" points="60,150 160,48 205,48 105,150"/>
    </svg>
    <div class="brand"><span class="brand-mark"></span>Brivond Technologies</div>
  </section>
</body>
</html>
```